Business Card & Stationary
Harbor Lane Finanical
Project: Business Card & Stationary
Business Card & Stationary - Financial Services
Creative Brief
Simple
Gordon Pelling
President
274 W. Larkspur Blvd. Suite 2260 Chicago, IL 60614
gpelling@harborlanefin.com
www.harborlanefin.com
The stationary should also be converted into a template for Word. We will get the business cards and envelopes printed but probably just use a laser printer for the stationary.
Some element of our logo .... make it look nice.

```html
<!DOCTYPE html>
<html lang="en">
<head>
<meta charset="utf-8">
<title>Harbor Lane Finanical — Business Card</title>
<link rel="stylesheet" href="https://fonts.googleapis.com/css2?family=Cinzel:wght@400&family=Crimson+Text:wght@400&display=swap">
<style>
  :root {
    --backdrop: #2e2d2c;
    --card: #ffffff;
    --brand-green: #6a7d2b;
    --ink: #5a5a5a;
    --rule: #b9b9b9;
  }
  * { box-sizing: border-box; margin: 0; padding: 0; }
  html, body { width: 1200px; height: 883px; overflow: hidden; }
  body { background: var(--backdrop); position: relative; font-family: "Crimson Text", Georgia, serif; }

  .card {
    position: absolute;
    width: 605px; height: 347px;
    background: var(--card);
    border-radius: 26px;
  }
  .card--front { left: 115px; top: 79px; }
  .card--back  { left: 478px; top: 468px; }

  .brand { position: absolute; left: 0; right: 0; text-align: center; }
  .brand__square { display: block; width: 48px; height: 48px; margin: 0 auto; background: var(--brand-green); }
  .brand__name {
    display: block; margin-top: 14px;
    font-family: "Cinzel", "Times New Roman", serif;
    font-size: 24px; letter-spacing: 0.5px; color: var(--brand-green);
    line-height: 1;
  }
  .card--front .brand { top: 34px; left: 170px; right: 80px; }
  .card--back .brand  { top: 132px; }

  .person { position: absolute; left: 232px; top: 146px; }
  .person__name { font-size: 27px; color: var(--brand-green); line-height: 1; }
  .person__title { font-size: 14px; color: var(--ink); margin-top: 8px; }

  .address {
    position: absolute; right: 313px; top: 272px;
    text-align: right; font-size: 14px; line-height: 20px; color: var(--ink);
    font-style: normal;
  }
  .divider { position: absolute; left: 300px; top: 236px; width: 1px; height: 104px; background: var(--rule); }

  .contacts { position: absolute; left: 310px; top: 238px; list-style: none; }
  .contacts li { display: flex; align-items: center; height: 20.5px; font-size: 13.5px; color: var(--ink); }
  .contacts svg { width: 14px; height: 14px; margin-right: 10px; fill: var(--brand-green); flex: none; }
</style>
</head>
<body>
  <section class="card card--front">
    <div class="brand">
      <span class="brand__square"></span>
      <span class="brand__name">Harbor Lane Finanical</span>
    </div>

    <div class="person">
      <div class="person__name">Gordon Pelling</div>
      <div class="person__title">President</div>
    </div>

    <address class="address">274 W. Larkspur Blvd.<br>Suite 2260<br>Chicago, IL 60614</address>
    <div class="divider"></div>

    <ul class="contacts">
      <li><svg viewBox="0 0 16 16" aria-hidden="true"><path d="M2 5c0-2 2-3 6-3s6 1 6 3v1h-3V5H5v1H2z M4 7h8l2 7H2z"/></svg>+1 (312) 555-0148</li>
      <li><svg viewBox="0 0 16 16" aria-hidden="true"><path d="M5 1h6a1 1 0 0 1 1 1v12a1 1 0 0 1-1 1H5a1 1 0 0 1-1-1V2a1 1 0 0 1 1-1zm1 2v8h4V3z"/></svg>+1 (312) 555-0172</li>
      <li><svg viewBox="0 0 16 16" aria-hidden="true"><path d="M4 1h7l2 2v3H4z M2 7h12v7H2z M5 9v2h6V9z"/></svg>+1 (312) 555-0193</li>
      <li><svg viewBox="0 0 16 16" aria-hidden="true"><path d="M1 3h14v10H1z M2 4l6 5 6-5v-.5H2z" fill-rule="evenodd"/></svg>gpelling@harborlanefin.com</li>
      <li><svg viewBox="0 0 16 16" aria-hidden="true"><circle cx="8" cy="8" r="6.5" fill="none" stroke="#6a7d2b" stroke-width="1.4"/><path d="M1.5 8h13M8 1.5c-3 3-3 10 0 13M8 1.5c3 3 3 10 0 13" fill="none" stroke="#6a7d2b" stroke-width="1.2"/></svg>www.harborlanefin.com</li>
    </ul>
  </section>

  <section class="card card--back">
    <div class="brand">
      <span class="brand__square"></span>
      <span class="brand__name">Harbor Lane Finanical</span>
    </div>
  </section>
</body>
</html>
```